Taking my business to the next level - going national and need new label design.

To begin, I need a label for my elderberry syrup kit and in the near future, I will need labels for five additional products as well as business cards. My companies name is Tamsel Grove, so named because we strongly believe plants have the power to maintain daily health and to provide healing during times of illness.
The elderberry kit should include the following information:
Logo - I can supply
Organic
Aronia & Elderberry
Power Blend
Syrup Kit
Daily Immunity
Allergy Support
It should be editable for different packages and quantities
This label will need to be: 3" tall by 5" wide

I need a second label for this product that measures 1.5" tall and 5" wide.
The second label should include:
our sustainability commitment statement
From our family to yours
makes 32 oz 105 ml
website address - this should stand out
www.TamselGroveCo.com

I am using a Kraft bag to package my product. It has a window on the front; one label will go above the window and the smaller of the two labels will go below.
I am drawn to the colors green and purple. The final design should communicate fresh, clean, and wellness

Health & wellness community, families

Supplement

• I like the font called KAZYcraie found on GlyphBarn - mentioned just as a sample

a54499
9bcb3c
ffc214

• See project description
Sustainability Commitment: (on the second label)
It is our guarantee to provide you with the highest ethical standards in sourcing quality, organic ingredients that support environmental sustainability in line with our commitment to health and wellness.
• no cartoon looks

```html
<!DOCTYPE html>
<html lang="en">
<head>
<meta charset="UTF-8">
<title>Tamsel Grove – Elderberry Syrup Kit Label</title>
<link rel="stylesheet" href="https://fonts.googleapis.com/css2?family=Itim&family=Poppins:wght@400;500&display=swap">
<style>
  :root {
    --backdrop: #c8c4c9;
    --label-white: #ffffff;
    --berry-purple: #a54499;
    --leaf-green: #3a9a2e;
    --ink: #222222;
    --pattern-lavender: #e4e2ef;
    --pattern-sage: #eef3ea;
  }
  html, body {
    margin: 0;
    padding: 0;
    width: 1200px;
    height: 1200px;
    overflow: hidden;
    background: var(--backdrop);
  }
  .canvas { display: block; width: 1200px; height: 1200px; }
  .label-title { font-family: "Itim", cursive; font-size: 80px; }
  .title-elderberry { fill: var(--berry-purple); }
  .title-syrup { fill: var(--leaf-green); }
  .benefit-text {
    font-family: "Poppins", sans-serif;
    font-size: 17px;
    fill: var(--label-white);
    text-anchor: middle;
    letter-spacing: 0.3px;
  }
  .kit-type {
    font-family: "Poppins", sans-serif;
    font-weight: 500;
    font-size: 29px;
    fill: var(--ink);
    text-anchor: middle;
  }
  .brand-name {
    font-family: "Poppins", sans-serif;
    font-weight: 500;
    font-size: 30px;
    fill: var(--ink);
  }
  .icon-disc { fill: var(--label-white); stroke: var(--berry-purple); stroke-width: 3; }
  .icon-mark { fill: none; stroke: var(--leaf-green); stroke-width: 2.6; stroke-linecap: round; stroke-linejoin: round; }
  .icon-fill { fill: var(--leaf-green); }
</style>
</head>
<body>
<svg class="canvas" viewBox="0 0 1200 1200" xmlns="http://www.w3.org/2000/svg">
  <defs>
    <clipPath id="label-shape">
      <path d="M71,388 Q599,196 1127,388 L1127,907 L71,907 Z"/>
    </clipPath>
    <linearGradient id="berry-wash" x1="0" y1="0" x2="1" y2="1">
      <stop offset="0" stop-color="var(--pattern-lavender)"/>
      <stop offset="0.5" stop-color="var(--pattern-sage)"/>
      <stop offset="1" stop-color="var(--pattern-lavender)"/>
    </linearGradient>
    <filter id="label-shadow" x="-5%" y="-5%" width="110%" height="115%">
      <feDropShadow dx="3" dy="5" stdDeviation="4" flood-color="#000" flood-opacity="0.35"/>
    </filter>
  </defs>

  <!-- label base -->
  <path class="label-base" d="M71,388 Q599,196 1127,388 L1127,907 L71,907 Z" fill="var(--label-white)" filter="url(#label-shadow)"/>

  <g clip-path="url(#label-shape)">
    <rect class="berry-pattern" role="img" aria-label="Faint pattern of elderberry clusters and leaves" x="71" y="290" width="1056" height="617" fill="url(#berry-wash)" opacity="0.75"/>
    <rect class="benefit-band" x="71" y="699" width="1056" height="122" fill="var(--berry-purple)" opacity="0.97"/>
  </g>

  <!-- inner frame -->
  <path class="label-frame" d="M83,398 Q599,214 1115,398 L1115,895 L83,895 Z" fill="none" stroke="var(--leaf-green)" stroke-width="2.5"/>

  <!-- brand -->
  <g class="brand">
    <circle cx="520" cy="428" r="13" fill="var(--leaf-green)"/>
    <text class="brand-name" x="542" y="439">Tamsel Grove</text>
  </g>

  <!-- title -->
  <text class="label-title" x="599" y="599" text-anchor="middle">
    <tspan class="title-elderberry">Elderberry</tspan>
    <tspan class="title-syrup">Syrup kit</tspan>
  </text>

  <!-- benefits -->
  <g class="benefit benefit-organic">
    <circle class="icon-disc" cx="284" cy="697" r="34"/>
    <path class="icon-mark" d="M268,711 h8 q8,0 14,-5 l8,-5 M268,716 h14 q6,0 12,-4 l8,-6"/>
    <path class="icon-mark" d="M284,703 v-18 M284,690 q-10,0 -12,-10 q10,0 12,10 M284,686 q8,-2 12,-12 q-10,0 -12,12"/>
  </g>
  <g class="benefit benefit-berries">
    <circle class="icon-disc" cx="441" cy="697" r="34"/>
    <circle class="icon-fill" cx="428" cy="700" r="7"/>
    <circle class="icon-fill" cx="443" cy="706" r="6"/>
    <circle class="icon-mark" cx="448" cy="690" r="4"/>
    <circle class="icon-mark" cx="456" cy="690" r="4"/>
    <circle class="icon-mark" cx="452" cy="698" r="4"/>
    <circle class="icon-mark" cx="444" cy="686" r="3"/>
  </g>
  <g class="benefit benefit-power">
    <circle class="icon-disc" cx="599" cy="697" r="34"/>
    <path class="icon-mark" d="M581,694 a18,18 0 0 1 30,-12 M617,700 a18,18 0 0 1 -30,12"/>
    <path class="icon-mark" d="M611,676 v7 h-7 M587,718 v-7 h7"/>
    <path class="icon-fill" d="M602,683 l-10,16 h7 l-3,12 l10,-16 h-7 z"/>
  </g>
  <g class="benefit benefit-immunity">
    <circle class="icon-disc" cx="756" cy="697" r="34"/>
    <path class="icon-fill" d="M756,677 l16,6 v10 q0,16 -16,24 q-16,-8 -16,-24 v-10 z"/>
    <circle cx="756" cy="696" r="7" fill="none" stroke="var(--label-white)" stroke-width="2"/>
    <path d="M756,692 v8 M752,696 h8" stroke="var(--label-white)" stroke-width="2" stroke-linecap="round"/>
  </g>
  <g class="benefit benefit-allergy">
    <circle class="icon-disc" cx="914" cy="697" r="34"/>
    <path class="icon-mark" d="M904,716 v-10 l-5,-8 v-6 M904,700 v-20 M910,698 v-22 M916,698 v-20 M922,700 v-14 v14 q0,10 -4,16 v4"/>
    <circle class="icon-fill" cx="910" cy="706" r="1.4"/>
    <circle class="icon-fill" cx="916" cy="710" r="1.4"/>
    <circle class="icon-fill" cx="908" cy="712" r="1.4"/>
  </g>

  <g class="benefit-labels">
    <text class="benefit-text" x="284" y="770">ORGANIC</text>
    <text class="benefit-text" x="441" y="770">ARONIA &amp;</text>
    <text class="benefit-text" x="441" y="794">ELDERBERRY</text>
    <text class="benefit-text" x="599" y="770">POWER</text>
    <text class="benefit-text" x="599" y="794">BLEND</text>
    <text class="benefit-text" x="756" y="770">DAILY</text>
    <text class="benefit-text" x="756" y="794">IMMUNITY</text>
    <text class="benefit-text" x="914" y="770">ALLERGY</text>
    <text class="benefit-text" x="914" y="794">SUPPORT</text>
  </g>

  <text class="kit-type" x="599" y="871">SYRUP KIT</text>
</svg>
</body>
</html>
```